Flyer für Beratung rund um den Computer
Zielgruppe
Hauptsächlich: Beratung rund um den Computer, individuelle Schulungen, technische Hilfe . Aber auch: Einführung in die Programmierung, Webseitenerstellung etc. Zielgruppe sind Privatpersonen, gerne auch ältere Personen, alle die sich unsicher im Umgang mit Computern fühlen und freundliche, geduldige Hilfe suchen.
Aufgabenstellung
Da meine Zielgruppe eher keine Computerfreaks sind, sollte der Flyer nicht zu technisch aussehen, sondern für Hilfesuchende ansprechend und freundlich wirken.

```html
<!DOCTYPE html>
<html lang="de">
<head>
<meta charset="utf-8">
<title>Technik ganz entspannt – Flyer</title>
<link rel="stylesheet" href="https://fonts.googleapis.com/css2?family=Josefin+Sans:wght@400;700&family=Poiret+One&display=swap">
<style>
  :root {
    --grey-dark: #7b7b7b;
    --grey-light: #d4d7d8;
    --cyan: #a9eff1;
    --ink: #1f1f1f;
    --tick: #8a8a8a;
    --photo-a: #3b4048;
    --photo-b: #a9a39c;
  }
  html, body { margin: 0; padding: 0; overflow: hidden; }
  body { width: 845px; height: 1200px; background: #fff; }
  .flyer {
    position: relative; width: 845px; height: 1200px; overflow: hidden;
    background: var(--grey-light); color: var(--ink);
    font-family: "Poiret One", sans-serif;
  }
  .backdrop { position: absolute; inset: 0; z-index: 0; }
  .brand {
    position: absolute; left: 530px; top: 100px; width: 260px; z-index: 2;
    text-align: center; color: var(--cyan);
    font-family: "Josefin Sans", sans-serif; font-weight: 700;
    font-size: 34px; letter-spacing: 5px; line-height: 1.25; text-transform: uppercase;
  }
  .tagline {
    position: absolute; left: 12px; top: 458px; margin: 0; z-index: 2;
    font-family: "Josefin Sans", sans-serif; font-weight: 400;
    font-variant: small-caps; font-size: 30px; letter-spacing: 0.5px;
  }
  .question-bubble {
    position: absolute; left: 8px; top: 569px; width: 242px; height: 242px; z-index: 1;
    border-radius: 50%; background: var(--cyan);
  }
  .shout {
    position: absolute; left: 28px; top: 520px; margin: 0; z-index: 3;
    font-family: "Poiret One", sans-serif; font-size: 56px; letter-spacing: 3px; line-height: 1;
    transform: rotate(-8deg); transform-origin: left bottom;
  }
  .question {
    position: absolute; left: 20px; top: 660px; margin: 0; z-index: 2;
    font-family: "Josefin Sans", sans-serif; font-variant: small-caps;
    font-size: 27px; line-height: 1.55;
  }
  .services { position: absolute; left: 305px; top: 592px; margin: 0; padding: 0; list-style: none; z-index: 2; }
  .services li { display: flex; align-items: center; height: 57px; font-size: 31px; }
  .services svg { width: 40px; height: 40px; margin-right: 10px; flex: none; }
  .interest {
    position: absolute; left: 218px; top: 872px; margin: 0; z-index: 2;
    font-size: 48px; transform: rotate(-7deg); transform-origin: left bottom;
  }
  .contact-title {
    position: absolute; left: 206px; top: 975px; margin: 0; z-index: 2;
    font-family: "Josefin Sans", sans-serif; font-variant: small-caps;
    font-weight: 400; font-size: 50px; letter-spacing: 2px;
  }
  .contact-line { position: absolute; left: 150px; display: flex; align-items: center; font-size: 22px; z-index: 2; }
  .contact-line svg { width: 38px; height: 30px; margin-right: 16px; }
  .contact-mail { top: 1037px; }
  .contact-phone { top: 1080px; }
  .hours { position: absolute; left: 205px; top: 1122px; margin: 0; font-size: 14px; line-height: 1.35; font-weight: 400; z-index: 2; }
  .hours span { display: block; }
  .hours .note { margin-top: 6px; }
</style>
</head>
<body>
<main class="flyer">
  <svg class="backdrop" width="845" height="1200" viewBox="0 0 845 1200">
    <defs>
      <linearGradient id="hands-photo" x1="0" y1="0" x2="1" y2="1">
        <stop offset="0" stop-color="#a9a39c"/>
        <stop offset="1" stop-color="#3b4048"/>
      </linearGradient>
      <linearGradient id="desk-photo" x1="0" y1="0" x2="1" y2="1">
        <stop offset="0" stop-color="#e7e2dc"/>
        <stop offset="1" stop-color="#6d6a66"/>
      </linearGradient>
    </defs>
    <path class="grey-dark-band" fill="#7b7b7b" d="M0,0 H845 V580 C760,560 690,470 560,440 C460,420 300,445 0,442 Z"/>
    <path class="hero-photo" role="img" aria-label="Foto: Hände an einem Laptop, ein Finger zeigt auf den Bildschirm" fill="url(#hands-photo)" d="M0,0 H525 V300 C525,380 480,415 395,415 H0 Z"/>
    <path class="cyan-strip" fill="#a9eff1" d="M845,560 C780,590 770,660 770,760 C770,830 720,855 640,855 L845,855 Z"/>
    <path class="cyan-footer" fill="#a9eff1" d="M0,885 C150,850 320,925 460,885 C600,840 700,855 845,830 V1200 H0 Z"/>
    <circle class="desk-photo" role="img" aria-label="Foto: Laptop und Kaffeetasse auf einem Holztisch" cx="712" cy="1045" r="136" fill="url(#desk-photo)"/>
  </svg>

  <div class="brand">Technik<br>ganz<br>entspannt</div>

  <p class="tagline">Computer- Alles, nur kein Hexenwissen</p>
  <div class="question-bubble"></div>
  <p class="shout">HILFE?!</p>
  <p class="question">Probleme<br>mit<br>dem Rechner?</p>

  <ul class="services">
    <li><svg viewBox="0 0 40 40"><rect x="2" y="2" width="36" height="36" rx="6" fill="#8a8a8a"/><path d="M10 21 L17 28 L30 13" fill="none" stroke="#fff" stroke-width="4" stroke-linecap="round" stroke-linejoin="round"/></svg>Beratung rund um Ihren Rechner</li>
    <li><svg viewBox="0 0 40 40"><rect x="2" y="2" width="36" height="36" rx="6" fill="#8a8a8a"/><path d="M10 21 L17 28 L30 13" fill="none" stroke="#fff" stroke-width="4" stroke-linecap="round" stroke-linejoin="round"/></svg>individuelle Schulungen</li>
    <li><svg viewBox="0 0 40 40"><rect x="2" y="2" width="36" height="36" rx="6" fill="#8a8a8a"/><path d="M10 21 L17 28 L30 13" fill="none" stroke="#fff" stroke-width="4" stroke-linecap="round" stroke-linejoin="round"/></svg>technische Hilfe</li>
    <li><svg viewBox="0 0 40 40"><rect x="2" y="2" width="36" height="36" rx="6" fill="#8a8a8a"/><path d="M10 21 L17 28 L30 13" fill="none" stroke="#fff" stroke-width="4" stroke-linecap="round" stroke-linejoin="round"/></svg>und vieles mehr</li>
  </ul>

  <p class="interest">Interesse?</p>
  <h2 class="contact-title">Kontakt:</h2>
  <div class="contact-line contact-mail">
    <svg viewBox="0 0 38 30"><rect x="2" y="3" width="34" height="24" rx="2" fill="none" stroke="#1f1f1f" stroke-width="2"/><path d="M2 4 L19 17 L36 4" fill="none" stroke="#1f1f1f" stroke-width="2"/></svg>
    mira@technik-ganz-entspannt.de
  </div>
  <div class="contact-line contact-phone">
    <svg viewBox="0 0 38 30"><path d="M9 2 L14 9 L11 13 C13 18 17 22 22 24 L26 21 L33 26 L29 29 C18 29 6 18 5 6 Z" fill="none" stroke="#1f1f1f" stroke-width="2" stroke-linejoin="round"/></svg>
    0151 238 7046
  </div>
  <p class="hours">
    <span>Montag bis Freitag 09:00 - 19:00 Uhr</span>
    <span>Samstag 09:00 - 14:00 Uhr</span>
    <span class="note">oder nach Vereinbarung</span>
  </p>
</main>
</body>
</html>
```